Web Design for One for One Organic Soap Company

We need a website design for the company Tidewell Botanics based on the package design per attached.

The design should communicate high end, luxury organic. The site will provide facts about how the spread of disease causes deaths and can be prevented with hand washing. The site will also have a page about why we are passionate about organics and how that relates to our skin including skin facts.
Also, the site should have an e-commerce product page and shopping cart.

Target Market(s)

Educated, health conscious and socially conscious consumers who shop luxury. Target vendors include Larkmont Grocers and Velbrook..

Industry/Entity Type

E-Commerce

Font styles to use
Other font styles liked:
• See attached

Requirements
Must have
• Use of Ying Yang leaf Logo provided.
Based on design provided.

```html
<!DOCTYPE html>
<html lang="en">
<head>
<meta charset="utf-8">
<title>Tidewell Botanics — Organic Soap</title>
<link href="https://fonts.googleapis.com/css2?family=Yanone+Kaffeesatz:wght@300;400&family=Open+Sans:wght@400;700&display=swap" rel="stylesheet">
<style>
:root{
  --bg:#f4f4f4;
  --panel:#ffffff;
  --ink:#2e2e2e;
  --muted:#555555;
  --rule:#d8d8d8;
  --green:#6c9c14;
  --green-light:#9cc42c;
  --green-dark:#4a7606;
  --logo-dark:#2f2f1f;
  --price:#d4201c;
  --sky:#cfe7f6;
  --hill:#a9c95a;
}
*{box-sizing:border-box;margin:0;padding:0}
html,body{width:1023px;height:1200px;overflow:hidden;background:var(--bg)}
body{position:relative;font-family:'Yanone Kaffeesatz',sans-serif;color:var(--ink)}
.abs{position:absolute}
.scene{position:absolute}
.header-scene{left:426px;top:0;width:597px;height:130px;background:linear-gradient(180deg,#bfe0f4 0%,#e8f3f9 55%,rgba(190,215,120,.6) 100%);border-bottom-left-radius:60% 30%}
.footer-scene{left:0;top:1066px;width:1023px;height:134px;background:linear-gradient(180deg,#dcedf7 0%,#c6e2f2 35%,#b6d26a 62%,#8fb339 100%)}
.brand{left:85px;top:13px;display:flex;align-items:center;gap:8px}
.brand-mark{width:53px;height:81px;background:var(--green)}
.brand-name{font-size:34px;font-weight:400;color:var(--logo-dark);letter-spacing:.5px}
.nav{left:85px;top:125px;width:853px;height:38px;border-top:1px solid #bdbdbd;border-bottom:1px solid #bdbdbd;background:linear-gradient(90deg,#fafafa,#f0f0f0)}
.nav a{position:absolute;top:8px;font-size:18px;color:#333;text-decoration:none;letter-spacing:1px;transform:translateX(-50%)}
.nav .active-bar{position:absolute;left:56px;top:-2px;width:75px;height:3px;background:var(--green)}
.box{position:absolute;background:var(--panel);left:85px;width:222px}
.box-head{position:absolute;left:0;top:0;width:222px;height:36px;border-top:1px solid var(--green);border-bottom:3px solid #a8c56a;background:var(--bg)}
.box-head span{position:absolute;left:17px;top:8px;font-size:17px;color:#333}
.cart-line{position:absolute;left:17px;width:190px;font-size:13px;color:var(--muted);border-bottom:1px solid #e2e2e2;padding-bottom:8px}
.cart-line b{color:var(--green)}
.btn{position:absolute;height:34px;border:2px solid #e6e6e6;background:linear-gradient(180deg,var(--green-light),var(--green-dark));color:#fff;font-size:20px;text-align:center;line-height:30px;box-shadow:0 0 0 1px #cfcfcf;letter-spacing:.5px}
.shop-list{position:absolute;left:17px;top:60px;width:190px;list-style:none}
.shop-list li{font-size:13px;color:var(--muted);height:26px;line-height:24px;border-bottom:1px solid #e2e2e2;padding-left:15px;position:relative}
.shop-list li:last-child{border-bottom:none}
.shop-list li::before{content:"";position:absolute;left:2px;top:9px;border:3px solid transparent;border-left:4px solid var(--green)}
.video{left:85px;top:656px;width:225px;height:171px;background:linear-gradient(135deg,#6b5a4e,#c9b8a6 50%,#3a3d44)}
.video-bar{position:absolute;left:7px;bottom:8px;width:211px;height:22px;background:rgba(0,0,0,.55)}
.slider{left:325px;top:186px;width:613px;height:351px;background:var(--panel);border-bottom:1px solid #ddd}
.slide-img{position:absolute;left:12px;top:13px;width:588px;height:328px;border:1px solid var(--green-light);background:linear-gradient(120deg,#f1d17a 0%,#e6b84c 45%,#f5e7d6 70%,#d3a88d 100%)}
.slide-caption{position:absolute;left:17px;top:190px;color:#fff;font-size:26px;line-height:38px;text-shadow:0 1px 2px rgba(0,0,0,.25)}
.slide-caption .big{font-size:34px}
.badge{left:299px;top:164px;width:144px;height:144px;border-radius:50%;border:3px solid var(--green-light);background:radial-gradient(circle at 60% 45%,#7b5a9a 0%,#c9a98b 45%,#f3ede6 80%)}
.dots{left:874px;top:545px;display:flex;gap:5px}
.dots i{width:8px;height:8px;border-radius:50%;background:var(--green)}
.dots i:first-child{background:#fff;border:1px solid #ddd}
.section-title{position:absolute;font-size:18px;color:#333;letter-spacing:.5px}
.section-rule{position:absolute;height:1px;background:#aaa}
.card{position:absolute;top:597px;height:253px;background:var(--panel);width:151px}
.card .thumb{position:absolute;left:15px;top:18px;width:134px;height:100px;border:1px solid var(--green-light)}
.card .name{position:absolute;left:21px;top:132px;font-size:17px;color:#333}
.card .price{position:absolute;left:21px;top:160px;font-size:17px;color:#333}
.card .price b{color:var(--price);font-weight:400;font-size:18px}
.card .btn{left:15px;top:196px;width:114px}
.about-text{position:absolute;left:88px;top:916px;width:845px;font-family:'Open Sans',sans-serif;font-size:10.4px;line-height:13.4px;color:#444}
.about-list{position:absolute;left:88px;top:978px;list-style:none;font-family:'Open Sans',sans-serif;font-size:10.4px;color:#444}
.about-list li{height:20.5px;padding-left:10px;position:relative}
.about-list li::before{content:"";position:absolute;left:0;top:3px;border:3px solid transparent;border-left:4px solid var(--green)}
.more{left:97px;top:1039px;font-family:'Open Sans',sans-serif;font-size:9px;font-weight:700;color:var(--green-dark)}
.footer-nav{left:0;width:1023px;top:1143px;text-align:center;font-size:13px;color:#222;letter-spacing:.5px}
.footer-nav span{margin:0 6px}
.social{left:0;width:1023px;top:1172px;text-align:center;font-size:15px;color:#fff}
.social span{margin:0 8px}
</style>
</head>
<body>

<div class="scene header-scene" role="img" aria-label="Illustrated sky with clouds, young trees and rolling green hills"></div>

<div class="abs brand">
  <div class="brand-mark"></div>
  <div class="brand-name">Tidewell Botanics</div>
</div>

<nav class="abs nav">
  <div class="active-bar"></div>
  <a style="left:89px">HOME</a>
  <a style="left:251px">ABOUT</a>
  <a style="left:409px">CONTACT</a>
  <a style="left:563px">STORES</a>
  <a style="left:735px">NATURAL SOAP</a>
</nav>

<section class="box" style="top:186px;height:198px">
  <div class="box-head"><span>Your Shoping</span></div>
  <div class="cart-line" style="top:55px">My Cart : <b>0</b> products</div>
  <div class="cart-line" style="top:89px">Organic bar soaps</div>
  <div class="cart-line" style="top:117px;border:none">Total : <b>$ 0</b></div>
  <div class="btn" style="left:54px;top:144px;width:111px">Details</div>
</section>

<section class="box" style="top:411px;height:205px">
  <div class="box-head"><span>Shop Online</span></div>
  <ul class="shop-list">
    <li>organic bar soaps</li>
    <li>castile liquid soaps</li>
    <li>organic balms &amp; oils</li>
    <li>unique handmade gifts</li>
    <li>timber &amp; coal for men</li>
  </ul>
</section>

<div class="abs" style="left:85px;top:645px;width:222px;height:1px;background:var(--green)"></div>
<div class="abs video" role="img" aria-label="Video still of a smiling woman with soap lather on her face">
  <div class="video-bar"></div>
</div>
<div class="abs" style="left:85px;top:843px;width:222px;height:8px;background:var(--panel)"></div>

<div class="abs slider">
  <div class="slide-img" role="img" aria-label="Stacked golden soap bars and lathered washing hands">
    <div class="slide-caption"><span class="big">Suitable</span> For Face ,Hair and Skin<br>Scented with <span class="big">Organic</span> Essential <span class="big">Oils</span></div>
  </div>
</div>
<div class="abs badge" role="img" aria-label="Lavender soap bars with purple flowers"></div>
<div class="abs dots"><i></i><i></i><i></i><i></i><i></i></div>

<div class="section-title" style="left:341px;top:567px">Feature Product</div>
<div class="section-rule" style="left:325px;top:593px;width:613px"></div>

<article class="card" style="left:325px">
  <div class="thumb" role="img" aria-label="Lavender soap bars" style="background:linear-gradient(120deg,#e9ddd2,#b89a86 50%,#6d4f8c)"></div>
  <div class="name">organic bar soaps</div>
  <div class="price">Price : <b>$20</b></div>
  <div class="btn">Buy</div>
</article>
<article class="card" style="left:478px">
  <div class="thumb" role="img" aria-label="Cream and herbal soap bars" style="background:linear-gradient(120deg,#fbf6ec,#f0d9a8 55%,#d8c78e)"></div>
  <div class="name">organic bar soaps</div>
  <div class="price">Price : <b>$20</b></div>
  <div class="btn">Buy</div>
</article>
<article class="card" style="left:632px">
  <div class="thumb" role="img" aria-label="Essential oil bottle with orange petals" style="background:linear-gradient(120deg,#5a3a1c,#c9741a 50%,#efe6d8)"></div>
  <div class="name">organic bar soaps</div>
  <div class="price">Price : <b>$20</b></div>
  <div class="btn">Buy</div>
</article>
<article class="card" style="left:785px">
  <div class="thumb" role="img" aria-label="Yellow and herb-speckled soap bars" style="background:linear-gradient(120deg,#e8d88a,#c9b25a 50%,#f1ecd6)"></div>
  <div class="name">organic bar soaps</div>
  <div class="price">Price : <b>$20</b></div>
  <div class="btn">Buy</div>
</article>

<div class="section-title" style="left:98px;top:875px">About</div>
<div class="section-rule" style="left:86px;top:903px;width:852px"></div>
<p class="about-text">Lorem ipsum dolor sit amet, consectetur adipiscing elit. Nulla at dui vitae metus fringilla congue eget et libero. Vivamus lobortis, metus placerat euismod dictum, justo purus eleifend leo, ac imperdiet ipsum dui at mauris.Pellentesque volutpat adipiscing tristique. Nullam varius felis lorem, nec adipiscing nisi. In nisl ipsum, aliquet sit amet auctor nec, facilisis ac dolor. Fusce pulvinar volutpat leo, eu iaculis leo rutrum eu. Nullam ultrices ultrices massa, a sollicitudin elit lobortis eget. Integer id rutrum velit. Nam pellentesque scelerisque felis non tempus.</p>
<ul class="about-list">
  <li>Lorem ipsum dolor sit amet, consectetur adipiscing elit.</li>
  <li>Nulla at dui vitae metus fringilla congue egeteto purus emperdiet ipsum dui at mauris.</li>
  <li>Lorem ipsum dolor sit arus emperdiet ipsuonsectetur adipiscing elit.</li>
</ul>
<div class="abs more">- MORE INFO -</div>

<div class="scene footer-scene" role="img" aria-label="Illustrated sky, young trees and rolling green hills"></div>
<div class="abs footer-nav"><span>HOME</span>|<span>ABOUT</span>|<span>CONTACT</span>|<span>STORES</span>|<span>NATURAL SOAP</span></div>
<div class="abs social"><span>Circlebook</span><span>Workring</span><span>ClipStream</span></div>

</body>
</html>
```